olive oil label for Brindlemoor Ridge Orchards, LLC

We need a logo/label design for our olive oil: Brindlemoor Ridge Orchards, LLC extra virgin olive oil: could be: Brindlemoor Ridge Oil. This is the first olive oil produced in Coastal Georgia since the colonists. Need a beautiful, simple label that will draw customers. I love the idea of a Verlaquet-type vessel with a drop of olive oil entering the vessel, and maybe an olive branch over that; but am open to whatever the designer chooses that will help us sell this very special, boutique-brand olive oil.

I'm still hoping for some new designs. The label is so important. I want a stylized, artistic label that is new and fresh looking, and will grab attention-a beautiful label that also looks like it is from Brindlemoor, GA. Thank you for your efforts!!!

Reason: I have not received a design label that I love yet, but there may be usable parts from a few. I have some suggestions that should help: I want a label that is beautiful, artistic, and is reminiscent of Brindlemoor, GA. Specifics: The bottle will be green, 10-1/2 inches tall, and look like this: https://www.quellorin.com/images/384512_903174455612038_519604233_o.jpg. I think the background color should look like mottled parchment paper. I would perhaps like 2 rows of stylized olive trees. In the middle of the 2 rows, perhaps a stylized (curvy "U" shaped) vessel with a drop of olive oil entering the vessel. The word, "Brindlemoor" should be the largest. Next largest: Extra Virgin. Next largest: Olive Oil. Followed by: first cold pressed, then: Produced by local family farm. The font for Brindlemoor should be similar to the font used by Thistlewick Hive Company.

I have not received a design label that I love yet, but there may be usable parts from a few. I have some suggestions that should help: I want a label that is beautiful, artistic, and is reminiscent of Brindlemoor, GA. Specifics: The bottle will be green, 10-1/2 inches tall, and look like this: https://www.quellorin.com/images/384512_903174455612038_519604233_o.jpg. I think the background color should look like mottled parchment paper. I would perhaps like 2 rows of stylized olive trees. In the middle of the 2 rows, perhaps a stylized (curvy "U" shaped) vessel with a drop of olive oil entering the vessel. The word, "Brindlemoor" should be the largest. Next largest: Extra Virgin. Next largest: Olive Oil. Followed by: first cold pressed, then: Produced by local family farm. The font for Brindlemoor should be similar to the font used by Thistlewick Hive Company.

I would like to extend my deadline for 2 days, to end January 9, 2014

```html
<!DOCTYPE html>
<html lang="en">
<head>
<meta charset="utf-8">
<title>Brindlemoor Extra Virgin Olive Oil – Label</title>
<link href="https://fonts.googleapis.com/css2?family=IM+Fell+DW+Pica+SC&family=Pinyon+Script&family=Cutive&display=swap" rel="stylesheet">
<style>
  :root {
    --backdrop-light: #9a9a9a;
    --backdrop-dark: #2a2a2a;
    --parchment: #cfc19d;
    --parchment-light: #ddd2b3;
    --parchment-dark: #b4a27a;
    --ink: #1c1a16;
    --ink-soft: #2b2822;
    --art-tone: #6f6650;
  }
  html, body {
    margin: 0;
    padding: 0;
    width: 1200px;
    height: 675px;
    overflow: hidden;
  }
  .stage {
    position: relative;
    width: 1200px;
    height: 675px;
    background: radial-gradient(ellipse at 50% 45%, var(--backdrop-light) 0%, #6a6a6a 45%, var(--backdrop-dark) 100%);
  }
  .label {
    position: absolute;
    left: 497px;
    top: 75px;
    width: 206px;
    height: 530px;
    border-radius: 103px;
    background:
      radial-gradient(circle at 30% 25%, rgba(255,255,255,0.18) 0%, transparent 35%),
      radial-gradient(circle at 75% 55%, rgba(120,100,60,0.22) 0%, transparent 30%),
      radial-gradient(circle at 20% 70%, rgba(120,100,60,0.18) 0%, transparent 28%),
      radial-gradient(circle at 60% 88%, rgba(255,255,255,0.15) 0%, transparent 30%),
      radial-gradient(circle at 85% 15%, rgba(120,100,60,0.15) 0%, transparent 25%),
      linear-gradient(180deg, var(--parchment-light), var(--parchment) 50%, var(--parchment-dark));
    box-shadow: inset 0 0 18px rgba(90,70,40,0.35);
    color: var(--ink);
  }
  .label-frame {
    position: absolute;
    inset: 12px 10px;
    border: 1.6px solid var(--ink);
    border-radius: 93px;
  }
  .branch-art {
    position: absolute;
    left: 22px;
    top: 6px;
    width: 150px;
    height: 136px;
    border-radius: 50% 50% 40% 40%;
    background: radial-gradient(ellipse at 45% 60%, var(--art-tone) 0%, rgba(111,102,80,0.55) 45%, transparent 72%);
  }
  .brand-name {
    position: absolute;
    top: 152px;
    left: 0;
    width: 100%;
    margin: 0;
    text-align: center;
    font-family: "Cutive", serif;
    font-weight: 400;
    font-size: 23px;
    line-height: 1;
    color: var(--ink);
  }
  .grade {
    position: absolute;
    top: 183px;
    left: 0;
    width: 100%;
    margin: 0;
    text-align: center;
    font-family: "IM Fell DW Pica SC", serif;
    font-size: 19px;
    line-height: 1;
  }
  .product {
    position: absolute;
    top: 203px;
    left: 0;
    width: 100%;
    margin: 0;
    text-align: center;
    font-family: "Pinyon Script", cursive;
    font-size: 17px;
    line-height: 1;
  }
  .vessel-art {
    position: absolute;
    left: 74px;
    top: 243px;
    width: 58px;
    height: 114px;
    border-radius: 18px 18px 10px 10px;
    background: radial-gradient(ellipse at 50% 68%, var(--art-tone) 0%, rgba(111,102,80,0.5) 45%, transparent 75%);
  }
  .claim {
    position: absolute;
    top: 372px;
    left: 0;
    width: 100%;
    margin: 0;
    text-align: center;
    font-family: "Cutive", serif;
    font-size: 12.5px;
    color: var(--ink-soft);
  }
  .origin {
    position: absolute;
    top: 397px;
    left: 0;
    width: 100%;
    margin: 0;
    text-align: center;
    font-family: "Cutive", serif;
    font-size: 9.5px;
    line-height: 1.45;
    color: var(--ink-soft);
  }
  .fine-print {
    position: absolute;
    top: 457px;
    left: 24px;
    right: 24px;
    display: flex;
    justify-content: space-between;
    font-family: "Cutive", serif;
    font-size: 8.5px;
    color: var(--ink-soft);
  }
  .lot-line {
    display: inline-block;
    width: 24px;
    border-bottom: 1px solid var(--ink-soft);
    margin-left: 3px;
  }
</style>
</head>
<body>
  <main class="stage">
    <section class="label">
      <div class="label-frame"></div>
      <div class="branch-art" role="img" aria-label="Engraved olive branch with two olives and leaves"></div>
      <h1 class="brand-name">Brindlemoor</h1>
      <p class="grade">Extra Virgin</p>
      <p class="product">Olive Oil</p>
      <div class="vessel-art" role="img" aria-label="Engraved oil vessel with a drop of olive oil falling into it"></div>
      <p class="claim">First cold pressed</p>
      <p class="origin">Produced in Coastal Georgia by<br>local family farm</p>
      <div class="fine-print">
        <span class="volume">17 fl oz</span>
        <span class="lot">Lot #<span class="lot-line"></span></span>
      </div>
    </section>
  </main>
</body>
</html>
```